Bref créative
Business Cards and Stationary for KRVMD
Modern
Warren Fitzhugh
Managing Partner
4185 Marlow Avenue, Suite 312
San Antonio TX 78249-6172
210-555-0148 x3092
warren@kr-vmd.example
www.kr-vmd.example
Logo Details
Font: Myriad Pro
Colors
BLUE C=85 M=50 Y=0 K=0
RED C=0 M=100 Y=100 K=0
GREY C=0 M=0 Y=0 K=90
Ai Logo Files

```html
<!DOCTYPE html>
<html lang="en">
<head>
<meta charset="utf-8">
<title>KRVMD Business Card</title>
<link rel="stylesheet" href="https://fonts.googleapis.com/css2?family=Source+Sans+3:wght@400;600;700&display=swap">
<style>
  :root {
    --blue: #1a7fcf;
    --blue-deep: #0c5aa6;
    --blue-light: #3aa6e8;
    --red: #e01b22;
    --grey: #333333;
    --paper: #ffffff;
    --backdrop: #e9e9e9;
  }
  * { margin: 0; padding: 0; box-sizing: border-box; }
  html, body { width: 1200px; height: 871px; overflow: hidden; }
  body {
    background: var(--backdrop);
    font-family: "Source Sans 3", "Myriad Pro", sans-serif;
    color: var(--grey);
    position: relative;
  }
  .card {
    position: absolute;
    left: 260px;
    width: 680px;
    height: 389px;
    border-radius: 4px;
    overflow: hidden;
    box-shadow: 0 6px 18px rgba(0,0,0,0.18);
  }
  .card-back {
    top: 31px;
    background: linear-gradient(135deg, var(--blue-light) 0%, var(--blue) 45%, var(--blue-deep) 100%);
    color: var(--paper);
    display: flex;
    flex-direction: column;
    align-items: center;
    justify-content: center;
  }
  .card-front { top: 451px; background: var(--paper); }

  .brand { display: flex; align-items: center; gap: 12px; }
  .brand-dot { width: 22px; height: 22px; border-radius: 50%; flex: none; }
  .brand-text { font-weight: 700; line-height: 1.05; }
  .brand-name { display: block; }
  .brand-sub { display: block; letter-spacing: 0.18em; }

  .card-back .brand-dot { background: var(--paper); width: 30px; height: 30px; }
  .card-back .brand-text { color: var(--paper); }
  .card-back .brand-name { font-size: 40px; }
  .card-back .brand-sub { font-size: 20px; margin-top: 4px; }
  .back-url {
    margin-top: 22px;
    font-size: 16px;
    letter-spacing: 0.12em;
    color: var(--paper);
  }

  .waves { position: absolute; right: 0; top: 0; width: 200px; height: 389px; }

  .card-front .brand { position: absolute; left: 44px; top: 64px; }
  .card-front .brand-dot { background: var(--blue); }
  .card-front .brand-text { color: var(--blue); }
  .card-front .brand-name { font-size: 27px; }
  .card-front .brand-sub { font-size: 14px; margin-top: 3px; }

  .person { position: absolute; left: 390px; top: 108px; }
  .person-name { font-size: 22px; font-weight: 600; color: var(--blue); }
  .person-title { font-size: 17px; color: var(--grey); margin-top: 2px; }

  .contact { position: absolute; left: 44px; top: 218px; font-size: 14px; line-height: 19px; }
  .address { margin-bottom: 8px; }
  .contact-list { list-style: none; }
  .contact-list li { display: flex; align-items: center; gap: 8px; }
  .icon { width: 12px; height: 12px; flex: none; fill: var(--red); }
</style>
</head>
<body>

<section class="card card-back">
  <div class="brand">
    <span class="brand-dot"></span>
    <span class="brand-text">
      <span class="brand-name">Marlow Lien Finance</span>
      <span class="brand-sub">KRVMD LLC</span>
    </span>
  </div>
  <p class="back-url">www.kr-vmd.example</p>
</section>

<section class="card card-front">
  <svg class="waves" viewBox="0 0 200 389" preserveAspectRatio="none" aria-hidden="true">
    <defs>
      <linearGradient id="bandBlue" x1="0" y1="0" x2="1" y2="1">
        <stop offset="0" stop-color="#3aa6e8"/>
        <stop offset="1" stop-color="#0c5aa6"/>
      </linearGradient>
    </defs>
    <path d="M200 0 L150 0 C60 90 200 210 110 389 L200 389 Z" fill="url(#bandBlue)"/>
    <path d="M128 0 C40 95 175 215 85 389 L96 389 C186 215 52 95 140 0 Z" fill="#e01b22"/>
  </svg>

  <div class="brand">
    <span class="brand-dot"></span>
    <span class="brand-text">
      <span class="brand-name">Marlow Lien Finance</span>
      <span class="brand-sub">KRVMD LLC</span>
    </span>
  </div>

  <div class="person">
    <p class="person-name">Warren Fitzhugh</p>
    <p class="person-title">Managing Partner</p>
  </div>

  <div class="contact">
    <p class="address">4185 Marlow Avenue, Suite 312<br>San Antonio TX 78249-6172</p>
    <ul class="contact-list">
      <li><svg class="icon" viewBox="0 0 12 12"><path d="M2 1h3l1 3-1.5 1a6 6 0 0 0 2.5 2.5L8 6l3 1v3a1 1 0 0 1-1 1A9 9 0 0 1 1 2a1 1 0 0 1 1-1z"/></svg>210-555-0148 x3092</li>
      <li><svg class="icon" viewBox="0 0 12 12"><rect x="3" y="0.5" width="6" height="11" rx="1.2"/></svg>914-555-0173</li>
      <li><svg class="icon" viewBox="0 0 12 12"><path d="M1 4h10v7H1z M3 1h6v3H3z"/></svg>866-555-0126</li>
      <li><svg class="icon" viewBox="0 0 12 12"><path d="M1 2h10v8H1z"/><path d="M1 2l5 4 5-4" stroke="#fff" fill="none"/></svg>warren@kr-vmd.example</li>
      <li><svg class="icon" viewBox="0 0 12 12"><circle cx="6" cy="6" r="5.5"/><path d="M0.5 6h11M6 0.5c-3 3-3 8 0 11M6 0.5c3 3 3 8 0 11" stroke="#fff" stroke-width="0.8" fill="none"/></svg>www.kr-vmd.example</li>
    </ul>
  </div>
</section>

</body>
</html>
```